YARD CRAFTERS "N" CO

catyering to driveway/patio floor construction and remodeling. Concrete, concrete pavers, asphalt, Landscaping, irrigation, pergolas and pools.

Target Market(s)

the home owner that wants to enhance their home

Industry/Entity Type

construction

Contact Information for Business Card

presidet: lino barrega email: yardcraftersnco@mailbox.test office/cell: 555 204 8813

Font styles to use
Sans Serif

Requirements
Must have
• logo should pop out
Nice to have
• the logo should demonstrate that we do exteriors only

```html
<!DOCTYPE html>
<html lang="en">
<head>
<meta charset="utf-8">
<title>Yard Crafters "N" Co — Business Card</title>
<link rel="stylesheet" href="https://fonts.googleapis.com/css2?family=Montserrat:wght@400;500;600&display=swap">
<style>
  :root {
    --page-bg: #e8e9eb;
    --card-bg: #2f4862;
    --card-pattern: #3a5572;
    --accent: #e3a449;
    --text-light: #f2f4f7;
    --icon-line: #c9d2dc;
  }
  * { box-sizing: border-box; margin: 0; padding: 0; }
  html, body {
    width: 1200px; height: 2200px; overflow: hidden;
    background: var(--page-bg);
    font-family: "Montserrat", Arial, sans-serif;
  }
  .sheet { position: relative; width: 1200px; height: 2200px; }
  .card {
    position: absolute; left: 60px; width: 1080px; height: 617px;
    background: var(--card-bg);
    overflow: hidden;
    box-shadow: 0 6px 18px rgba(20, 30, 45, 0.18);
  }
  .card--services { top: 330px; }
  .card--contact { top: 1250px; }

  .pattern {
    position: absolute;
    background: linear-gradient(135deg, var(--card-bg) 0%, var(--card-pattern) 55%, var(--card-bg) 100%);
    opacity: 0.9;
  }
  .card--services .pattern--top { top: 0; left: 0; width: 1080px; height: 90px; }
  .card--services .pattern--bottom { right: 0; bottom: 0; width: 560px; height: 150px; }
  .card--contact .pattern--top { top: 0; right: 0; width: 520px; height: 80px; }
  .card--contact .pattern--bottom { right: 0; bottom: 0; width: 620px; height: 120px; }

  .brand {
    position: absolute; left: 70px; top: 180px; width: 440px;
    color: var(--text-light);
    text-align: center;
  }
  .brand__mark {
    width: 120px; height: 120px;
    border: 4px solid var(--text-light);
    margin: 0 auto 34px;
  }
  .brand__name {
    font-weight: 400; font-size: 27px; letter-spacing: 2px;
    white-space: nowrap;
  }

  .services { position: absolute; left: 590px; top: 182px; }
  .services__title {
    color: var(--accent); font-weight: 500;
    font-size: 23px; letter-spacing: 1.5px; line-height: 1.3;
    margin-bottom: 22px;
  }
  .services__list { list-style: none; }
  .services__item {
    display: flex; align-items: center; gap: 22px;
    color: var(--text-light); font-size: 25px; line-height: 1;
    margin-bottom: 19px;
  }
  .services__item svg { width: 20px; height: 24px; flex: none; }

  .person { position: absolute; left: 590px; top: 170px; }
  .person__name {
    color: var(--accent); font-weight: 500; font-size: 38px; letter-spacing: 3px;
    text-transform: uppercase;
  }
  .person__role {
    color: var(--text-light); font-size: 21px; letter-spacing: 2px;
    margin-top: 6px; margin-bottom: 34px;
  }
  .contact { list-style: none; }
  .contact__item {
    display: flex; align-items: center; gap: 22px;
    color: var(--text-light); font-size: 24px;
    margin-bottom: 22px;
  }
  .contact__icon { width: 26px; height: 26px; flex: none; }
</style>
</head>
<body>
<main class="sheet">

  <section class="card card--services">
    <div class="pattern pattern--top" role="img" aria-label="Faint woven-tile pattern band"></div>
    <div class="pattern pattern--bottom" role="img" aria-label="Faint woven-tile pattern corner"></div>

    <div class="brand">
      <div class="brand__mark"></div>
      <p class="brand__name">YARD CRAFTERS "N" CO</p>
    </div>

    <div class="services">
      <h2 class="services__title">DRIVEWAY, PATIO FLOOR<br>CONSTRUCTION &amp; REMODELING</h2>
      <ul class="services__list">
        <li class="services__item"><svg viewBox="0 0 20 24"><path d="M10 22s-7-7.5-7-12.5a7 7 0 0 1 14 0C17 14.5 10 22 10 22z" fill="none" stroke="var(--icon-line)" stroke-width="2"/><circle cx="10" cy="9.5" r="2.5" fill="none" stroke="var(--icon-line)" stroke-width="2"/></svg>Concrete</li>
        <li class="services__item"><svg viewBox="0 0 20 24"><path d="M10 22s-7-7.5-7-12.5a7 7 0 0 1 14 0C17 14.5 10 22 10 22z" fill="none" stroke="var(--icon-line)" stroke-width="2"/><circle cx="10" cy="9.5" r="2.5" fill="none" stroke="var(--icon-line)" stroke-width="2"/></svg>Concrete pavers</li>
        <li class="services__item"><svg viewBox="0 0 20 24"><path d="M10 22s-7-7.5-7-12.5a7 7 0 0 1 14 0C17 14.5 10 22 10 22z" fill="none" stroke="var(--icon-line)" stroke-width="2"/><circle cx="10" cy="9.5" r="2.5" fill="none" stroke="var(--icon-line)" stroke-width="2"/></svg>Asphalt</li>
        <li class="services__item"><svg viewBox="0 0 20 24"><path d="M10 22s-7-7.5-7-12.5a7 7 0 0 1 14 0C17 14.5 10 22 10 22z" fill="none" stroke="var(--icon-line)" stroke-width="2"/><circle cx="10" cy="9.5" r="2.5" fill="none" stroke="var(--icon-line)" stroke-width="2"/></svg>Landscaping</li>
        <li class="services__item"><svg viewBox="0 0 20 24"><path d="M10 22s-7-7.5-7-12.5a7 7 0 0 1 14 0C17 14.5 10 22 10 22z" fill="none" stroke="var(--icon-line)" stroke-width="2"/><circle cx="10" cy="9.5" r="2.5" fill="none" stroke="var(--icon-line)" stroke-width="2"/></svg>Irrigation</li>
        <li class="services__item"><svg viewBox="0 0 20 24"><path d="M10 22s-7-7.5-7-12.5a7 7 0 0 1 14 0C17 14.5 10 22 10 22z" fill="none" stroke="var(--icon-line)" stroke-width="2"/><circle cx="10" cy="9.5" r="2.5" fill="none" stroke="var(--icon-line)" stroke-width="2"/></svg>Pergolas and pools.</li>
      </ul>
    </div>
  </section>

  <section class="card card--contact">
    <div class="pattern pattern--top" role="img" aria-label="Faint woven-tile pattern band"></div>
    <div class="pattern pattern--bottom" role="img" aria-label="Faint woven-tile pattern band"></div>

    <div class="brand">
      <div class="brand__mark"></div>
      <p class="brand__name">YARD CRAFTERS "N" CO</p>
    </div>

    <div class="person">
      <h1 class="person__name">Lino Barrega</h1>
      <p class="person__role">PRESIDENT</p>
      <ul class="contact">
        <li class="contact__item">
          <svg class="contact__icon" viewBox="0 0 24 24"><path d="M6.6 3.5l3 3.2-1.9 2.4a12 12 0 0 0 7.2 7.2l2.4-1.9 3.2 3-1.7 3.1C11 20 4 13 3.5 5.2z" fill="none" stroke="var(--icon-line)" stroke-width="1.8" stroke-linejoin="round"/></svg>
          555 204 8813
        </li>
        <li class="contact__item">
          <svg class="contact__icon" viewBox="0 0 24 24"><rect x="3" y="5.5" width="18" height="13" fill="none" stroke="var(--icon-line)" stroke-width="1.8"/><path d="M3 6l9 7 9-7" fill="none" stroke="var(--icon-line)" stroke-width="1.8"/></svg>
          yardcraftersnco@mailbox.test
        </li>
        <li class="contact__item">
          <svg class="contact__icon" viewBox="0 0 24 24"><circle cx="12" cy="12" r="9" fill="none" stroke="var(--icon-line)" stroke-width="1.8"/><ellipse cx="12" cy="12" rx="4" ry="9" fill="none" stroke="var(--icon-line)" stroke-width="1.5"/><path d="M3 12h18" stroke="var(--icon-line)" stroke-width="1.5"/></svg>
          www.yardcraftersnco.test
        </li>
      </ul>
    </div>
  </section>

</main>
</body>
</html>
```